General Dental Office Business Card

I run a private general dental office in southern California, and would like a refresh/redesign of my business card. I focus on quality care rather than volume. The email address on the uploaded current card should be updated to: info@marbleshoredental.example. The current card's logo is a deboss, but I am open to other ideas. The logo can be refreshed, but it is something that's been with me since the beginning of the office, so I wouldn't want a drastic redesign.
Target Market(s)
Adults 18-99, whoever needs dental services
Industry/Entity Type
Healthcare/Dental
Contact Information for Business Card
Name, Address, Phone, email
Colors
Designer to choose colors to be used in the design.
Requirements
Must have
- Logo (Same as original one in the uploaded file), space on back for appointment time/date

```html
<!DOCTYPE html>
<html lang="en">
<head>
<meta charset="utf-8">
<title>Marble Shore Dental – Business Card</title>
<link href="https://fonts.googleapis.com/css2?family=Questrial&display=swap" rel="stylesheet">
<style>
  :root {
    --navy: #0d3f66;
    --sky: #6cc0dd;
    --ink: #3d3d3d;
    --rule: #5a82a3;
    --paper: #ffffff;
    --paper-shade: #eeeeee;
    --backdrop: #d9dadc;
  }
  * { margin: 0; padding: 0; box-sizing: border-box; }
  html, body {
    width: 1200px; height: 900px; overflow: hidden;
    background: var(--backdrop);
    font-family: "Questrial", sans-serif;
  }
  .card {
    position: absolute;
    width: 630px; height: 360px;
    background: linear-gradient(120deg, var(--paper-shade), var(--paper));
    overflow: hidden;
    box-shadow: 0 6px 18px rgba(0,0,0,.18);
  }
  .card--appointment { left: 70px; top: 50px; }
  .card--contact { left: 500px; top: 490px; }

  .decor { position: absolute; top: 0; height: 100%; }
  .card--appointment .decor { left: 0; width: 260px; }
  .card--contact .decor { right: 0; width: 300px; }

  .appointment-title {
    position: absolute; right: 70px; top: 34px;
    color: var(--navy); font-size: 15px; font-weight: 400; letter-spacing: .5px;
  }
  .appointment-field {
    position: absolute; display: flex; align-items: flex-end;
    color: var(--sky); font-size: 14px;
  }
  .appointment-field .line {
    flex: 1; margin-left: 8px; margin-bottom: 4px;
    border-bottom: 1.5px dotted var(--sky);
  }
  .field-date { left: 280px; right: 40px; top: 66px; }
  .field-time { left: 340px; right: 40px; top: 106px; }

  .brand-large {
    position: absolute; left: 236px; top: 196px;
    color: var(--sky); font-size: 46px; font-weight: 400; line-height: 1.1;
    letter-spacing: 1px; white-space: nowrap;
  }
  .brand-large .second { display: block; padding-left: 30px; }

  .brand-small {
    position: absolute; left: 40px; top: 40px;
    display: flex; align-items: center; gap: 14px;
    color: var(--sky); font-size: 24px; line-height: 1.05; white-space: nowrap;
  }
  .brand-small .mark {
    width: 58px; height: 58px; border-radius: 50%;
    border: 3px solid var(--sky); flex: none;
  }
  .brand-small .second { display: block; padding-left: 20px; }

  .person { position: absolute; left: 44px; top: 140px; }
  .person-name { color: var(--sky); font-size: 20px; }
  .person-role { color: var(--ink); font-size: 16px; margin-top: 2px; }

  .contacts {
    position: absolute; left: 44px; top: 214px;
    list-style: none; color: var(--ink); font-size: 15px;
  }
  .contacts li { display: flex; align-items: center; gap: 10px; height: 24px; white-space: nowrap; }
  .contacts svg { width: 16px; height: 16px; fill: none; stroke: var(--sky); stroke-width: 1.8; }

  .divider {
    position: absolute; left: 44px; width: 360px; top: 296px;
    border-top: 1.5px solid var(--rule);
  }
  .address {
    position: absolute; left: 44px; top: 306px;
    color: var(--ink); font-size: 15px; white-space: nowrap;
  }
</style>
</head>
<body>

<section class="card card--appointment">
  <svg class="decor" viewBox="0 0 260 360" preserveAspectRatio="none" role="img" aria-label="Palm tree decoration in navy and light blue">
    <path d="M0 0 H150 C120 80 110 200 180 360 H0 Z" fill="#0d3f66"/>
    <path d="M150 0 C120 80 110 200 180 360 H170 C104 200 114 80 144 0 Z" fill="#6cc0dd"/>
  </svg>
  <h2 class="appointment-title">YOUR APPOINTMENT</h2>
  <div class="appointment-field field-date">Date<span class="line"></span></div>
  <div class="appointment-field field-time">Time<span class="line"></span></div>
  <h1 class="brand-large">MARBLE<span class="second">SHORE DENTAL</span></h1>
</section>

<section class="card card--contact">
  <svg class="decor" viewBox="0 0 300 360" preserveAspectRatio="none" role="img" aria-label="Palm tree decoration in navy and light blue">
    <path d="M0 0 H300 V360 H250 C240 220 170 80 0 0 Z" fill="#0d3f66"/>
    <path d="M0 0 C170 80 240 220 250 360 H240 C230 224 162 86 0 0 Z" fill="#6cc0dd"/>
  </svg>
  <div class="brand-small">
    <span class="mark"></span>
    <span>MARBLE<span class="second">SHORE DENTAL</span></span>
  </div>
  <div class="person">
    <p class="person-name">Dr. Daniel R. Lowe DDS</p>
    <p class="person-role">General Dentistry</p>
  </div>
  <ul class="contacts">
    <li><svg viewBox="0 0 16 16"><path d="M4 1.5 L6.5 4.5 L5 6 C6 8 8 10 10 11 L11.5 9.5 L14.5 12 L12.5 14.5 C7 13.5 2.5 9 1.5 3.5 Z"/></svg>(555) 014-7391</li>
    <li><svg viewBox="0 0 16 16"><rect x="1.5" y="3.5" width="13" height="9"/><path d="M1.5 3.5 L8 9 L14.5 3.5"/></svg>info@marbleshoredental.example</li>
    <li><svg viewBox="0 0 16 16"><circle cx="8" cy="8" r="6.5"/><path d="M1.5 8 H14.5 M8 1.5 C5 5 5 11 8 14.5 M8 1.5 C11 5 11 11 8 14.5"/></svg>www.marbleshoredental.example</li>
  </ul>
  <div class="divider"></div>
  <p class="address">1180 Harbor Crest Way, Marble Shore, CA 90000</p>
</section>

</body>
</html>
```